Business Card Design

Lanternfield Recruitment is a specialist financial services recruitment company and implementation partner

Industry/Entity Type

Business

Contact Information for Business Card

Tom Hadley
Lanternfield Recruiment Ltd
e:tom.hadley@lanternfield-recruitment.example
m:07723 408 316
m:07844 251 903
s: tommhadley

```html
<!DOCTYPE html>
<html lang="en">
<head>
<meta charset="utf-8">
<title>Lanternfield Recruitment – Business Card</title>
<link rel="stylesheet" href="https://fonts.googleapis.com/css2?family=Open+Sans:wght@400;600;700;800&display=swap">
<style>
  :root {
    --bg: #e9e6e2;
    --band: #2b2b2d;
    --band-edge: #3d3d40;
    --teal: #1fb5ad;
    --ink: #3a3a3c;
    --paper: #ffffff;
  }
  * { box-sizing: border-box; margin: 0; padding: 0; }
  html, body { width: 1200px; height: 913px; overflow: hidden; }
  body {
    background: var(--bg);
    font-family: "Open Sans", Arial, sans-serif;
    color: var(--ink);
    display: flex;
    flex-direction: column;
    align-items: center;
    justify-content: center;
    gap: 56px;
  }
  .card {
    position: relative;
    width: 600px;
    height: 343px;
    background: var(--paper);
    box-shadow: 0 10px 24px rgba(0,0,0,.18);
    overflow: hidden;
  }
  .band {
    position: absolute;
    left: 0; right: 0;
    height: 46px;
    background: linear-gradient(180deg, var(--band-edge), var(--band));
  }
  .band--top { top: 0; border-bottom: 4px solid var(--teal); }
  .band--bottom { bottom: 0; border-top: 4px solid var(--teal); }

  .wordmark {
    display: flex;
    align-items: center;
    gap: 10px;
    color: var(--teal);
    font-weight: 800;
    text-transform: uppercase;
    line-height: 1.05;
  }
  .wordmark__dot {
    width: 30px; height: 30px;
    border-radius: 50%;
    background: var(--teal);
    flex: none;
  }
  .wordmark__text { display: flex; flex-direction: column; }
  .wordmark__main { font-size: 30px; letter-spacing: .5px; }
  .wordmark__sub { font-size: 13px; letter-spacing: 1.5px; }

  .card--front .wordmark {
    position: absolute;
    left: 50%; top: 50%;
    transform: translate(-50%, -50%);
  }

  .card--back .wordmark {
    position: absolute;
    left: 48px; top: 196px;
  }
  .card--back .wordmark__main { font-size: 24px; }
  .card--back .wordmark__sub { font-size: 11px; }

  .contact {
    position: absolute;
    left: 312px; top: 74px;
    width: 262px;
  }
  .contact__name {
    font-size: 20px;
    font-weight: 400;
    text-transform: uppercase;
    letter-spacing: .5px;
    padding-bottom: 6px;
    border-bottom: 1.5px solid var(--teal);
  }
  .contact__name strong { font-weight: 800; }
  .contact__list { list-style: none; margin-top: 14px; }
  .contact__row {
    display: flex;
    align-items: center;
    gap: 12px;
    margin-bottom: 12px;
    font-size: 11px;
    line-height: 1.35;
  }
  .contact__icon {
    width: 30px; height: 22px;
    border-radius: 4px;
    background: var(--teal);
    flex: none;
    display: flex; align-items: center; justify-content: center;
  }
  .contact__icon svg { width: 13px; height: 13px; }
</style>
</head>
<body>

  <section class="card card--front" aria-label="Card front">
    <div class="band band--top"></div>
    <div class="wordmark">
      <span class="wordmark__dot"></span>
      <span class="wordmark__text">
        <span class="wordmark__main">Lanternfield</span>
        <span class="wordmark__sub">Recruiment Ltd</span>
      </span>
    </div>
    <div class="band band--bottom"></div>
  </section>

  <section class="card card--back" aria-label="Card back">
    <div class="band band--top"></div>

    <div class="wordmark">
      <span class="wordmark__dot"></span>
      <span class="wordmark__text">
        <span class="wordmark__main">Lanternfield</span>
        <span class="wordmark__sub">Recruiment Ltd</span>
      </span>
    </div>

    <div class="contact">
      <h1 class="contact__name"><strong>Tom</strong> Hadley</h1>
      <ul class="contact__list">
        <li class="contact__row">
          <span class="contact__icon">
            <svg viewBox="0 0 24 24" fill="#fff"><path d="M6.6 10.8a15.1 15.1 0 0 0 6.6 6.6l2.2-2.2a1 1 0 0 1 1-.25 11.4 11.4 0 0 0 3.6.57 1 1 0 0 1 1 1V20a1 1 0 0 1-1 1A17 17 0 0 1 3 4a1 1 0 0 1 1-1h3.5a1 1 0 0 1 1 1c0 1.25.2 2.45.57 3.57a1 1 0 0 1-.25 1z"/></svg>
          </span>
          <span>07723 408 316<br>07844 251 903</span>
        </li>
        <li class="contact__row">
          <span class="contact__icon">
            <svg viewBox="0 0 24 24" fill="none" stroke="#fff" stroke-width="2"><circle cx="12" cy="12" r="9"/><path d="M3 12h18M12 3c3 3 3 15 0 18M12 3c-3 3-3 15 0 18"/></svg>
          </span>
          <span>lanternfield-recruitment.example<br>tom.hadley@lanternfield-recruitment.example</span>
        </li>
        <li class="contact__row">
          <span class="contact__icon"></span>
          <span>tommhadley</span>
        </li>
      </ul>
    </div>

    <div class="band band--bottom"></div>
  </section>

</body>
</html>
```